Vornix Store > Into Website

Hello - this is our Vornix Store
https://www.vornix-market.example/stores/BRINDLEWAVE/page/7D4183A2-B91E-42FC-95D8-AEED318572FA?ref_=vbx_qtm
I need someone to use the text from out listings, he details, and description PLUS the images here and create a very simple but modern website designed as a brochure / shopping / feature site.

All [Add to Cart] buttons will jump to Vornix, so this site is designed as a web presence for the Vornix Store.

Domain will be www.BrindleWave.example

Nav Link:
About Setup Instructions Tutorials FAQ Contact

Ideal candidate will have experience working with ecommerce, and working with detailed listings. All the details on the Vornix listings page are important (size / weight /etc) so it's a challenge to make all this readable and friendly.

Please be ready to start immediately and ready to delivery code-ready Figma files within a week.

```html
<!DOCTYPE html>
<html lang="en">
<head>
<meta charset="utf-8">
<title>Stabilize and Prevent Future Injuries</title>
<link rel="stylesheet" href="https://fonts.googleapis.com/css2?family=Open+Sans:wght@400;700&display=swap">
<style>
  :root {
    --page-bg: #e0e0e0;
    --panel-bg: #ffffff;
    --heading: #333333;
    --body-text: #3a3a3a;
    --accent: #6a4cf5;
    --photo-sky: #dfe5ea;
    --photo-mid: #b9b6d6;
    --photo-ground: #a8a39c;
  }
  * { box-sizing: border-box; margin: 0; padding: 0; }
  html, body {
    width: 1200px;
    height: 611px;
    overflow: hidden;
    background: var(--page-bg);
    font-family: "Open Sans", Arial, sans-serif;
  }
  .benefits {
    position: relative;
    width: 1200px;
    height: 611px;
  }
  .benefits__title {
    position: absolute;
    top: 72px;
    left: 0;
    width: 100%;
    text-align: center;
    font-size: 30px;
    font-weight: 700;
    color: var(--heading);
    letter-spacing: 0.1px;
  }
  .benefit-tab {
    position: absolute;
    top: 155px;
    width: 74px;
    height: 385px;
    background: var(--panel-bg);
  }
  .benefit-tab--traction { left: 70px; }
  .benefit-tab--strength { left: 158px; }
  .benefit-tab--flexibility { left: 246px; }
  .benefit-tab__label {
    position: absolute;
    left: 50%;
    bottom: 22px;
    writing-mode: vertical-rl;
    transform: translateX(-50%) rotate(180deg);
    font-size: 15px;
    font-weight: 700;
    color: var(--accent);
    letter-spacing: 0.3px;
  }
  .benefit-photo {
    position: absolute;
    top: 155px;
    left: 334px;
    width: 367px;
    height: 385px;
    background: linear-gradient(180deg, var(--photo-sky) 0%, var(--photo-sky) 55%, var(--photo-mid) 75%, var(--photo-ground) 100%);
  }
  .benefit-detail {
    position: absolute;
    top: 155px;
    left: 701px;
    width: 429px;
    height: 385px;
    background: var(--panel-bg);
    text-align: center;
  }
  .benefit-detail__name {
    position: absolute;
    top: 151px;
    left: 0;
    width: 100%;
    font-size: 16px;
    font-weight: 700;
    color: var(--heading);
    letter-spacing: 0.3px;
  }
  .benefit-detail__text {
    position: absolute;
    top: 193px;
    left: 50%;
    width: 320px;
    transform: translateX(-50%);
    font-size: 13px;
    line-height: 24px;
    color: var(--body-text);
  }
</style>
</head>
<body>
  <section class="benefits">
    <h1 class="benefits__title">Stabilize and Prevent Future Injuries</h1>

    <div class="benefit-tab benefit-tab--traction"><span class="benefit-tab__label">TRACTION</span></div>
    <div class="benefit-tab benefit-tab--strength"><span class="benefit-tab__label">STRENGTH</span></div>
    <div class="benefit-tab benefit-tab--flexibility"><span class="benefit-tab__label">FLEXIBILITY</span></div>

    <div class="benefit-photo" role="img" aria-label="Woman in an inverted backbend pose in a purple aerial yoga hammock hung from an outdoor frame"></div>

    <div class="benefit-detail">
      <h2 class="benefit-detail__name">BALANCE</h2>
      <p class="benefit-detail__text">Asymmetrical, dynamic poses are a fun way to correct right-left imbalances.</p>
    </div>
  </section>
</body>
</html>
```